Flyer-Design für IT Firma
Zielgruppe
Wir sind eine IT Firma aus München und möchten unsere Dienstleistung vermarkten. Unsere Zielgruppe sind hauptsächlich Endkunden und kleinere Firmen.
Aufgabenstellung
Ich habe mal einen Flyer gesehen der ebenfalls IT Dienstleistung beworben hat und in Kachelform mit kleinen Icons zu den Dienstleistungen aufgebaut war. War ganz schön aber ist nicht zwingend. Gerne lassen wir uns von neuen Vorschlägen überraschen.
Format war A6 Doppelseitig angedacht. Falls sich ein anderes Format besser eignet sind wir auch dafür offen.
Den Inhalt habe ich als Word Datei hoch geladen.
Das Logo habe ich leider nicht als EI oder APS Datei, und somit auch nur als Word Datei hoch geladen. Jedes Element ist aber einzeln bearbeitbar. Falls in Verbindung mit dem Flyer Design eine leichte Modernisierung des Logos notwendig ist, wäre das kein Problem.

```html
<!DOCTYPE html>
<html lang="de">
<head>
<meta charset="utf-8">
<title>Flyer Vorderseite – Lokaler Computer Service</title>
<link rel="stylesheet" href="https://fonts.googleapis.com/css2?family=Arimo:wght@400;700&family=Nunito:wght@800&family=Varela+Round&display=swap">
<style>
  :root{
    --stage:#d9dce0;
    --ink-dark:#1c1c1c;
    --ink-deep:#111111;
    --panel:#1f1f1f;
    --brand-blue:#0b6fc6;
    --accent-blue:#1a78d4;
    --white:#ffffff;
    --photo-a:#2a2b2d;
    --photo-b:#707378;
    --visual-a:#13a9c8;
    --visual-b:#0b3fd0;
  }
  html,body{margin:0;padding:0;width:896px;height:1200px;overflow:hidden;background:var(--stage);}
  .flyer{position:absolute;left:26px;top:0;width:844px;height:1200px;overflow:hidden;background:var(--ink-dark);}
  .flyer-art{position:absolute;inset:0;width:844px;height:1200px;}
  .flyer-text{position:absolute;margin:0;color:var(--white);}
  .since{left:587px;top:66px;font:700 20px/1 "Arimo",sans-serif;}
  .headline{font:700 44px/40px "Arimo",sans-serif;letter-spacing:.5px;}
  .headline--consult{left:54px;top:211px;}
  .headline--local{left:54px;top:466px;}
  .service-title{position:absolute;margin:0;color:var(--accent-blue);font:800 17px/23px "Nunito",sans-serif;}
  .service-body{position:absolute;margin:0;color:var(--white);font:400 16.5px/20px "Varela Round",sans-serif;}
  .tagline{left:55px;top:1121px;font:400 16.5px/20px "Arimo",sans-serif;}
  .brand-name{left:627px;top:1046px;font:700 46px/1 "Arimo",sans-serif;letter-spacing:3px;}
</style>
</head>
<body>
<main class="flyer">
  <svg class="flyer-art" viewBox="0 0 1262 1793" preserveAspectRatio="none" xmlns="http://www.w3.org/2000/svg">
    <defs>
      <linearGradient id="photoTone" x1="0" y1="0" x2="1" y2="0.3">
        <stop offset="0" stop-color="var(--photo-a)"/>
        <stop offset="1" stop-color="var(--photo-b)"/>
      </linearGradient>
      <linearGradient id="visualTone" x1="0" y1="1" x2="1" y2="0">
        <stop offset="0" stop-color="var(--visual-a)"/>
        <stop offset=".55" stop-color="var(--visual-b)"/>
        <stop offset="1" stop-color="#0a2fa8"/>
      </linearGradient>
    </defs>

    <rect class="hero-photo" x="0" y="0" width="1262" height="1040" fill="url(#photoTone)" role="img" aria-label="Foto: Hand tippt auf eine digitale Oberfläche"/>
    <polygon class="panel-top-left" points="0,0 470,0 470,960 0,960" fill="var(--ink-dark)"/>
    <polygon class="panel-top-right" points="830,0 1262,0 1262,140 830,290" fill="var(--ink-dark)"/>

    <rect class="hero-visual" x="488" y="95" width="494" height="602" fill="url(#visualTone)" opacity=".92" role="img" aria-label="Illustration: Glühbirne in einem Haus, blau getönt"/>

    <polygon class="band-consult" points="0,300 478,170 478,497 0,630" fill="var(--brand-blue)"/>

    <polygon class="area-services" points="0,1033 235,950 1262,738 1262,1793 0,1793" fill="var(--ink-deep)"/>
    <polygon class="panel-local" points="0,685 478,530 495,860 0,1033" fill="var(--panel)"/>
    <line class="divider-line" x1="235" y1="951" x2="1262" y2="739" stroke="var(--white)" stroke-width="6"/>

    <g class="service-icons" fill="none" stroke="var(--accent-blue)" stroke-width="5" stroke-linecap="round" stroke-linejoin="round">
      <g class="icon-lock">
        <rect x="158" y="1010" width="70" height="70" rx="12"/>
        <path d="M173 1010 V990 A20 20 0 0 1 213 990 V1010"/>
        <circle cx="193" cy="1040" r="8"/>
        <line x1="193" y1="1048" x2="193" y2="1060"/>
      </g>
      <g class="icon-gear">
        <path d="M445 942 L465 942 L469 955 L481 960 L493 953 L507 967 L500 979 L505 991 L518 995 L518 1015 L505 1019 L500 1031 L507 1043 L493 1057 L481 1050 L469 1055 L465 1068 L445 1068 L441 1055 L429 1050 L417 1057 L403 1043 L410 1031 L405 1019 L392 1015 L392 995 L405 991 L410 979 L403 967 L417 953 L429 960 L441 955 Z"/>
        <circle cx="455" cy="1005" r="12"/>
      </g>
      <g class="icon-edit">
        <path d="M730 888 H705 A12 12 0 0 0 693 900 V948 A12 12 0 0 0 705 960 H753 A12 12 0 0 0 765 948 V925"/>
        <path d="M757 876 L772 891 L737 926 L718 930 L722 911 Z"/>
      </g>
      <g class="icon-mail">
        <rect x="963" y="845" width="78" height="60" rx="10"/>
        <path d="M963 862 L1002 878 L1041 862"/>
      </g>
    </g>

    <polygon class="band-white" points="0,1675 1262,1250 1262,1793 0,1793" fill="var(--white)"/>
    <polygon class="panel-tagline" points="0,1688 645,1473 968,1793 0,1793" fill="var(--panel)"/>
    <polygon class="panel-brand" points="712,1520 1262,1335 1262,1793 1000,1793" fill="var(--brand-blue)"/>
  </svg>

  <p class="flyer-text since">seit über 20 Jahren</p>
  <h1 class="flyer-text headline headline--consult">BERATUNG<br>COMPUTER<br>SERVICE</h1>
  <h2 class="flyer-text headline headline--local">LOKALER<br>COMPUTER<br>SERVICE</h2>

  <section class="service service--recovery">
    <h3 class="service-title" style="left:55px;top:749px;">Daten-<br>wiederherstellung</h3>
    <p class="service-body" style="left:54px;top:805px;">Rettung verloren<br>gegangener Daten<br>bei Hard- &amp; Software<br>DefektTausch von<br>Hard- &amp; Software um<br>Performance auf<br>alten Systemen zu<br>erhöhen</p>
  </section>

  <section class="service service--support">
    <h3 class="service-title" style="left:252px;top:733px;">Service</h3>
    <p class="service-body" style="left:252px;top:771px;">Hilfe bei Problemen<br>mit E-Mail<br>Programmen und<br>Providern</p>
    <p class="service-body" style="left:252px;top:862px;">Hilfe bei vielen<br>Weiteren IT &amp; EDV<br>Problemen einfach<br>nachfragen</p>
  </section>

  <section class="service service--repair">
    <h3 class="service-title" style="left:440px;top:699px;">Display &amp; Tastatur<br>Reparatur</h3>
    <p class="service-body" style="left:440px;top:758px;">Tausch defekter<br>Notebook<br>Komponenten</p>
  </section>

  <section class="service service--malware">
    <h3 class="service-title" style="left:627px;top:670px;">Viren &amp; Malware<br>Beseitigung</h3>
    <p class="service-body" style="left:627px;top:729px;">Entfernung<br>Schadsoftware und<br>Bereinigung des<br>Betriebssystems</p>
  </section>

  <p class="flyer-text tagline">Ihr zuverlässiger Partner für Hard- &amp; Software Produkte<br>und IT &amp; EDV Dienstleistung in München</p>
  <p class="flyer-text brand-name">KARVO</p>
</main>
</body>
</html>
```